Looking for a modern website banner design

Bramblecrest Coaching Partners looking for the development of the main banner of the website. The project description and photos are included in the upload files.

```html
<!DOCTYPE html>
<html lang="en">
<head>
<meta charset="utf-8">
<title>Bramblecrest Coaching Partners – Banner</title>
<link rel="stylesheet" href="https://fonts.googleapis.com/css2?family=Barlow+Semi+Condensed:ital,wght@1,600&family=Open+Sans:wght@400;600&display=swap">
<style>
  :root {
    --navy: #0c1b26;
    --blue: #1a8fd6;
    --blue-deep: #0a5fa8;
    --white: #ffffff;
    --rule: #c9d3da;
  }
  * { margin: 0; padding: 0; box-sizing: border-box; }
  html, body { width: 1200px; height: 562px; overflow: hidden; background: var(--navy); }
  .banner {
    position: relative;
    width: 1200px;
    height: 562px;
    background: var(--navy);
    overflow: hidden;
    font-family: "Open Sans", sans-serif;
    color: var(--white);
  }
  .banner__art { position: absolute; inset: 0; width: 1200px; height: 562px; }
  .brand {
    position: absolute;
    left: 62px;
    top: 64px;
    display: flex;
    align-items: center;
    gap: 10px;
  }
  .brand__dot {
    width: 18px; height: 18px; border-radius: 50%;
    background: var(--white);
  }
  .brand__name {
    font-family: "Open Sans", sans-serif;
    font-weight: 600;
    font-size: 22px;
    letter-spacing: 0.3px;
    color: var(--white);
  }
  .testimonial {
    position: absolute;
    left: 56px;
    top: 168px;
    width: 660px;
  }
  .testimonial__quote {
    font-family: "Barlow Semi Condensed", sans-serif;
    font-style: italic;
    font-weight: 600;
    font-size: 23.5px;
    line-height: 36px;
    letter-spacing: -0.2px;
  }
  .testimonial__highlight { color: var(--blue); }
  .testimonial__credit {
    display: flex;
    align-items: center;
    margin-top: 26px;
    font-size: 17.5px;
    font-weight: 400;
    letter-spacing: -0.2px;
  }
  .testimonial__credit span + span {
    border-left: 1px solid var(--rule);
    margin-left: 14px;
    padding-left: 14px;
  }
</style>
</head>
<body>
<main class="banner">
  <svg class="banner__art" viewBox="0 0 1200 562" aria-hidden="false">
    <defs>
      <linearGradient id="corner-glow" x1="0" y1="0" x2="1" y2="1">
        <stop offset="0" stop-color="#1aa0ea"/>
        <stop offset="1" stop-color="#0b5ea8"/>
      </linearGradient>
      <linearGradient id="arena-top" x1="0" y1="0" x2="1" y2="1">
        <stop offset="0" stop-color="#3a2a2e"/>
        <stop offset="0.45" stop-color="#7a2a30"/>
        <stop offset="0.75" stop-color="#d9dde2"/>
        <stop offset="1" stop-color="#e9eef3"/>
      </linearGradient>
      <linearGradient id="arena-bench" x1="0" y1="0" x2="1" y2="1">
        <stop offset="0" stop-color="#b3262e"/>
        <stop offset="0.5" stop-color="#2a2f3a"/>
        <stop offset="1" stop-color="#5a2a2c"/>
      </linearGradient>
    </defs>

    <polygon class="accent accent--corner" points="0,428 162,562 0,562" fill="url(#corner-glow)"/>
    <polygon class="accent accent--bar-top" points="770,0 812,0 775,45 739,45" fill="var(--blue)"/>

    <g role="img" aria-label="Player celebrating a goal on the ice in front of a cheering arena crowd">
      <polygon points="841,0 1200,0 1200,378 1112,466 747,97" fill="url(#arena-top)"/>
    </g>
    <g role="img" aria-label="Smiling player high-fiving teammates along the bench">
      <polygon points="887,275 1175,562 600,562" fill="url(#arena-bench)" stroke="var(--navy)" stroke-width="14" stroke-linejoin="miter"/>
    </g>

    <polygon class="accent accent--bar-bottom" points="587,512 619,512 569,562 537,562" fill="var(--blue)"/>
  </svg>

  <div class="brand">
    <span class="brand__dot"></span>
    <span class="brand__name">Bramblecrest Coaching Partners</span>
  </div>

  <section class="testimonial">
    <p class="testimonial__quote">“Bramblecrest has provided support that has allowed me to develop as a person and an athlete. <span class="testimonial__highlight">The P.A.C.E.™</span> process allowed me to stay focused on attainable goals each season and progress from Junior to College and now Professional Hockey.”</p>
    <p class="testimonial__credit">
      <span>Marcus Delacroix</span>
      <span>Riverton Blizzards</span>
      <span>Atlantic Pro Hockey League</span>
    </p>
  </section>
</main>
</body>
</html>
```